Letterhead for SaaS

Design a letterhead that aligns with our new business card, using our logo and color scheme and text defined in the Branding Guide to ensure consistency. Consider incorporating a subtle watermark for added elegance. The layout should reflect the card's style, creating a cohesive look across our stationery.

```html
<!DOCTYPE html>
<html lang="en">
<head>
<meta charset="utf-8">
<title>Vortella Letterhead</title>
<link href="https://fonts.googleapis.com/css2?family=Exo+2:wght@800&family=Saira+Condensed:wght@400&family=Montserrat:wght@400&display=swap" rel="stylesheet">
<style>
:root{
  --bg:#f5f6f8;
  --paper:#f5f6f8;
  --navy:#0f1a2e;
  --navy-2:#17284a;
  --teal:#2e7fa0;
  --cyan:#3ab4e6;
  --ink:#1c1f26;
  --accent:#e0457b;
}
*{margin:0;padding:0;box-sizing:border-box}
html,body{width:1027px;height:1200px;overflow:hidden;background:var(--bg)}
.letterhead{
  position:absolute;left:167px;top:111px;width:694px;height:981px;
  background:var(--paper);
  box-shadow:0 2px 10px rgba(0,0,0,.45);
  overflow:hidden;
  font-family:"Saira Condensed",sans-serif;color:var(--ink);
}
.header-band{
  position:absolute;left:0;top:0;width:531px;height:144px;
  background:linear-gradient(120deg,var(--navy-2),var(--navy) 60%,#0b1424);
}
.header-title{
  position:absolute;left:47px;top:28px;
  font-family:"Exo 2",sans-serif;font-weight:800;font-size:82px;line-height:1;
  color:var(--teal);letter-spacing:1px;
}
.brand-name{
  position:absolute;right:22px;top:157px;
  font-family:"Exo 2",sans-serif;font-weight:800;font-size:30px;line-height:1;color:var(--navy);
}
.sender{position:absolute;left:45px;top:226px;}
.sender-name{font-size:14px;color:var(--cyan);line-height:20px}
.sender-role{font-size:11px;line-height:18px;margin-bottom:4px}
.sender-line{font-size:14.5px;line-height:21px}
.sender-line .key{color:var(--cyan)}
.sender-line .key.dark{color:var(--ink)}
.sender-line .sep{color:var(--accent);font-size:9px;margin:0 4px}
.sender-line .sep.dark{color:var(--ink)}
.date{position:absolute;right:43px;top:284px;font-size:14.5px;line-height:21px}
.body-text{position:absolute;left:45px;top:346px;width:610px;font-size:14.8px;line-height:27px}
.body-text p{margin-bottom:27px}
.footer-rule{position:absolute;left:82px;top:855px;width:529px;height:2px;background:var(--navy)}
.footer-rule::before{content:"";position:absolute;left:0;top:0;width:50px;height:2px;background:var(--cyan)}
.contact{
  position:absolute;top:883px;display:flex;align-items:center;gap:7px;
  font-family:"Montserrat",sans-serif;font-size:13px;color:var(--ink);
}
.contact svg{stroke:var(--cyan);fill:none;stroke-width:1.4}
.footer-band{
  position:absolute;left:0;bottom:0;width:100%;height:47px;
  background:linear-gradient(120deg,var(--navy-2),var(--navy) 55%,#0b1424);
}
</style>
</head>
<body>
<main class="letterhead">
  <div class="header-band" role="img" aria-label="Dark navy faceted geometric pattern"></div>
  <div class="header-title">VORTELLA</div>
  <div class="brand-name">VORTELLA</div>

  <section class="sender">
    <div class="sender-name">MARA LINHOLT</div>
    <div class="sender-role">CHIEF DIRECTOR</div>
    <div class="sender-line"><span class="key">A</span><span class="sep">:</span>12-4,HARBOR LANE KESTREL – 4410</div>
    <div class="sender-line"><span class="key dark">W</span><span class="sep dark">:</span>MAIL@VORTELLA.COM, WWW.VORTELLA.COM</div>
    <div class="sender-line"><span class="key">P</span><span class="sep">:</span>+880 – 55501 – 2468</div>
  </section>
  <div class="date">DATE, 10 SEPTEMBER, 2020</div>

  <section class="body-text">
    <p>THIS IS A SAMPLE LETTER THAT HAS BEEN PLACED TO DEMONSTRATE TYPING REMAT (YOUR COMPANY). LETTERHEAD DESIGN. WHEN POSITIONED PROPERLY, IT WILL SERVE TO WORK IN HARMONY WITH ALL OTHER ELEMENTS LETTERHEAD. THIS LETTERHEAD DESIGN IS MEANT TO PROJECT AN IMAGE</p>
    <p>THIS LETTERHEAD DESIGN IS MEANT PROJECT AN IMAGE OF PROFESSIONALISM RELIABILITY. BY USING SIMPLE ALIGEN WE HAVE CREATED A VERY SPACIOUS FEELING. THE SIMPLICITY SUGGEST RENGTHTHE SPACIOUSNES CONTRIBUTES H AESTHETICS THE LAYOUT. THESE BASIC QUALITIES ALONG WITH THE (YOUR COMPANY)</p>
    <p>LOOK AND HELPS REINFORCE THE (YOUR COMPANY) BRAND. LETTERHEAD DESIGN IS MEANT TO PROJECT AN IMAGE P DESIGN. WHEN POSITIONED PROPERLY, IT WILL SERVE TO WORK IN HARMONY ALL THE OTHER ELEMENTS LETTERHEAD. SIONALISM AND RELIABILITY.</p>
    <p>THIS LETTERHEAD DESIGN IS BASED ON THE (FORM OF YOUR LOGO) FORM (YOUR COMPANY) LOGO. EACH STATIONERY WE HAVE CREATED A VERY SPACIOUS FEELING. THE SIMPLICITY SUGGESTS STRENGTH THE SPACIOUSNES CONTRIBUTE PART OF THE (FORM OF YOUR LOGO).</p>
  </section>

  <div class="footer-rule"></div>
  <div class="contact" style="left:94px">
    <svg width="21" height="30" viewBox="0 0 21 30"><rect x="1" y="1" width="19" height="28" rx="2"/><line x1="1" y1="5" x2="20" y2="5"/><line x1="1" y1="25" x2="20" y2="25"/></svg>
    <span>(555) 014-2290</span>
  </div>
  <div class="contact" style="left:261px;gap:11px">
    <svg width="27" height="20" viewBox="0 0 27 20"><rect x="1" y="1" width="25" height="18" rx="1"/><polyline points="1,1 13.5,11 26,1"/><line x1="1" y1="19" x2="10" y2="9"/><line x1="26" y1="19" x2="17" y2="9"/></svg>
    <span>nadia.k@vortella.com</span>
  </div>
  <div class="contact" style="left:471px;gap:9px">
    <svg width="25" height="25" viewBox="0 0 25 25"><circle cx="12.5" cy="12.5" r="11.5"/><ellipse cx="12.5" cy="12.5" rx="5" ry="11.5"/><line x1="1" y1="12.5" x2="24" y2="12.5"/><line x1="12.5" y1="1" x2="12.5" y2="24"/></svg>
    <span>www.vortella.com</span>
  </div>

  <div class="footer-band" role="img" aria-label="Dark navy faceted geometric pattern"></div>
</main>
</body>
</html>
```